Crestline Slate & Tile Needs a Business Card

Attached you will find your logo, my photo and design guidelines for a new business card. The final design will need two separate files to create an embossed card. The cards will be printed by www.plinkprint.com (Instructions below)
Format is the Zib SQUARE card
Crestline Slate And Tile is a brick and mortar, retail stone and tile shop.
One the front:
Crestline Slate And Tile
Gerald Finchcombe
Owner
48207 Vesper Hollow Blvd
Suite R & T
Charlotte, NC 28953
Cell: 704-555-0183
Web: www.CrestlineSlateAndTile.com
(Make each word of the domain a different or alternating color)
On the back;
Something that shows beautiful colorful tile
Follow the design guide closely please. For more information see this page that describes creating the spot gloss file: https://www.plinkprint.com/us/business-cards/design-guidelines-spot-gloss
The logo is what we would like to have raised spot glossed.
Format is the Zib SQUARE card. See attahced guidlines.

```html
<!DOCTYPE html>
<html lang="en">
<head>
<meta charset="utf-8">
<title>Crestline Slate &amp; Tile – Business Card</title>
<link rel="stylesheet" href="https://fonts.googleapis.com/css2?family=Cinzel:wght@500;600&family=Montserrat:wght@400;500&display=swap">
<style>
  :root {
    --page: #d6d6d6;
    --paper: #ede6da;
    --navy: #1f3340;
    --rust: #a9452a;
    --gold: #b98a3a;
    --photo-dark: #2f3338;
    --photo-mid: #6b5a52;
  }
  * { margin: 0; padding: 0; box-sizing: border-box; }
  html, body { width: 1200px; height: 720px; overflow: hidden; }
  body {
    background: var(--page);
    position: relative;
    font-family: "Montserrat", sans-serif;
    color: var(--navy);
  }
  .card {
    position: absolute;
    top: 132px;
    width: 456px;
    height: 456px;
    background: var(--paper);
    box-shadow: 0 6px 14px rgba(0,0,0,0.18);
  }
  .card--front { left: 124px; }
  .card--back { left: 620px; }

  .portrait {
    position: absolute;
    left: 0; top: 0;
    width: 227px; height: 227px;
    background: linear-gradient(160deg, var(--photo-dark) 0%, #4a4642 55%, var(--photo-mid) 100%);
  }
  .person {
    position: absolute;
    left: 253px; top: 74px;
  }
  .person__name {
    font-family: "Cinzel", serif;
    font-weight: 600;
    font-size: 22px;
    line-height: 30px;
    letter-spacing: 1px;
    color: var(--navy);
  }
  .person__title {
    margin-top: 8px;
    font-size: 17px;
    letter-spacing: 3px;
    color: var(--rust);
    font-weight: 400;
  }

  .brand {
    position: absolute;
    display: flex;
    align-items: center;
  }
  .brand__mark { background: var(--gold); flex: none; }
  .brand__name {
    font-family: "Cinzel", serif;
    font-weight: 500;
    color: var(--navy);
    white-space: nowrap;
  }
  .brand--front { left: 36px; top: 252px; gap: 16px; }
  .brand--front .brand__mark { width: 56px; height: 56px; }
  .brand--front .brand__name { font-size: 24px; line-height: 30px; letter-spacing: 3px; }
  .brand--front .brand__line2 { font-size: 16px; letter-spacing: 6px; }

  .contact {
    position: absolute;
    left: 146px; top: 330px;
    list-style: none;
    font-size: 14.5px;
    line-height: 22px;
    letter-spacing: 0.6px;
    color: var(--navy);
  }
  .contact li { position: relative; padding-left: 24px; }
  .contact svg { position: absolute; left: 0; top: 3px; width: 16px; height: 16px; fill: var(--rust); }
  .web__alt { color: var(--rust); }

  .brand--back {
    left: 0; right: 0; top: 96px;
    flex-direction: column;
    gap: 34px;
  }
  .brand--back .brand__mark { width: 100px; height: 100px; }
  .brand--back .brand__name { text-align: center; font-size: 46px; line-height: 52px; letter-spacing: 5px; }
  .brand--back .brand__line2 { font-size: 24px; letter-spacing: 10px; }
</style>
</head>
<body>
  <section class="card card--front">
    <div class="portrait" role="img" aria-label="Portrait photo of Gerald Finchcombe, owner"></div>

    <div class="person">
      <h1 class="person__name">Gerald<br>Finchcombe</h1>
      <p class="person__title">OWNER</p>
    </div>

    <div class="brand brand--front">
      <span class="brand__mark"></span>
      <div class="brand__name">
        <div>CRESTLINE</div>
        <div class="brand__line2">SLATE &amp; TILE</div>
      </div>
    </div>

    <ul class="contact">
      <li>
        <svg viewBox="0 0 16 16" aria-hidden="true"><path d="M8 0a6 6 0 0 0-6 6c0 4.5 6 10 6 10s6-5.5 6-10a6 6 0 0 0-6-6zm0 8.5A2.5 2.5 0 1 1 8 3.5a2.5 2.5 0 0 1 0 5z"/></svg>
        48207 Vesper Hollow Blvd<br>Suite R &amp; T, Charlotte, NC 28953
      </li>
      <li>
        <svg viewBox="0 0 16 16" aria-hidden="true"><path d="M3.6 1l2.3 2.9-1.3 1.9c.9 2 2.6 3.7 4.6 4.6l1.9-1.3L14 11.4l-1.3 2.4C7 13.6 2.4 9 2.2 3.3z"/></svg>
        704-555-0183
      </li>
      <li>
        <svg viewBox="0 0 16 16" aria-hidden="true"><path d="M8 1a7 7 0 1 0 0 14A7 7 0 0 0 8 1zm0 1.3c.8.8 1.5 2.2 1.7 3.9H6.3C6.5 4.5 7.2 3.1 8 2.3zM2.4 7.4h2.7c0 .5 0 .9.1 1.2H2.4a5.7 5.7 0 0 1 0-1.2zm3.9 0h3.4v1.2H6.3zm4.6 0h2.7a5.7 5.7 0 0 1 0 1.2h-2.7zM8 13.7c-.8-.8-1.5-2.2-1.7-3.9h3.4c-.2 1.7-.9 3.1-1.7 3.9z"/></svg>
        <span>Crestline</span><span class="web__alt">Slate</span><span>And</span><span class="web__alt">Tile</span><span>.com</span>
      </li>
    </ul>
  </section>

  <section class="card card--back">
    <div class="brand brand--back">
      <span class="brand__mark"></span>
      <div class="brand__name">
        <div>CRESTLINE</div>
        <div class="brand__line2">SLATE &amp; TILE</div>
      </div>
    </div>
  </section>
</body>
</html>
```